Line of Premium Pelmeni and Perogies of supermarkets

A new company on the block looking for a unique design. A premium brand of perogies and pelmeni.
The price of the product is directed towards the upper to the middle class. the packaging price will be 20$ while you can find competitors at 8$, the packaging needs to reflect that.
attached is also the vector file of the logo of the company currently, it must be displayed prominently. (Dorvik)
there is a whole line of products, the design should be easily adjustable for different flavours.
the flavours are:
Perogies:
potato
potato/musrooms
cottage cheese
potato/feta/parsley
mushrooms/beef
Dumplings (pemini) :
veal
veal/chicken
chicken
veal/pork
chicken/veal/pork
the product uses the most quality meat and hand-made quality.
we are looking for a premium feel and a unique design that stands out.
please refer to the example of similar products we like, and please be as creative as you can.
we really like the one example, where the flavour (beef for instance) where the cow is the shape of the window.
we are looking for talented designers who are able to think outside of the (pelmeni) box.

```html
<!DOCTYPE html>
<html lang="en">
<head>
<meta charset="UTF-8">
<title>Dorvik Perogies – Potato/Feta/Parsley</title>
<link href="https://fonts.googleapis.com/css2?family=Lato:wght@400;700;900&family=Oswald:wght@500;600&display=swap" rel="stylesheet">
<style>
  :root{
    --bg:#ece7df;
    --sleeve-black:#0b0b0b;
    --brand-yellow:#f7bd1c;
    --cream:#efe8d2;
    --cream-dark:#d9cfb0;
    --white:#ffffff;
    --logo-ring:#6b4a2e;
  }
  *{margin:0;padding:0;box-sizing:border-box}
  html,body{width:1200px;height:1200px;overflow:hidden;background:var(--bg)}
  .canvas{position:relative;width:1200px;height:1200px}
  .sleeve{position:absolute;left:200px;top:60px;width:800px;height:1081px;background:var(--sleeve-black);font-family:"Lato",sans-serif;color:var(--white);overflow:hidden}
  .side-bar{position:absolute;top:150px;width:91px;height:73px;background:var(--brand-yellow)}
  .side-bar--left{left:0}
  .side-bar--right{right:0}
  .seal{position:absolute;top:150px;width:110px;text-align:center;color:var(--brand-yellow);font-family:"Oswald",sans-serif;font-weight:600;line-height:1}
  .seal--quality{left:118px;font-size:22px}
  .seal--natural{left:590px;top:160px;font-size:24px}
  .seal--natural .seal__big{font-size:30px}
  .seal svg{display:block;margin:0 auto 3px}
  .brand{position:absolute;left:266px;top:60px;width:268px;height:268px;text-align:center}
  .brand__circle{position:absolute;left:34px;top:0;width:200px;height:200px;border-radius:50%;background:var(--logo-ring)}
  .brand__name{position:absolute;left:0;right:0;top:212px;font-family:"Lato",sans-serif;font-weight:900;font-size:44px;letter-spacing:3px;color:var(--white)}
  .tagline{position:absolute;top:346px;left:0;right:0;text-align:center;color:var(--brand-yellow);font-size:17px;letter-spacing:1.2px;font-weight:400}
  .window-frame{position:absolute;left:93px;top:392px;width:629px;height:240px;background:var(--brand-yellow);border-radius:22px 22px 0 0}
  .window{position:absolute;left:118px;top:414px;width:583px;height:201px;border-radius:10px 10px 0 0;background:linear-gradient(160deg,var(--cream) 0%,var(--cream-dark) 60%,var(--cream) 100%)}
  .flavour-band{position:absolute;left:0;top:615px;width:800px;height:332px;background:var(--brand-yellow)}
  .product-name{position:absolute;left:0;right:0;top:638px;text-align:center;color:var(--sleeve-black);font-weight:900;font-size:104px;line-height:1;letter-spacing:1px}
  .flavour{position:absolute;left:0;right:0;top:742px;text-align:center;color:var(--sleeve-black);font-weight:400;font-size:46px;line-height:1;letter-spacing:1px}
  .claims{position:absolute;left:112px;top:808px;width:586px;height:139px;background:var(--sleeve-black);border-radius:16px 16px 0 0;padding:24px 0 0 54px}
  .claims__title{color:var(--brand-yellow);font-weight:700;font-size:21px;letter-spacing:.5px}
  .claims__rule{width:470px;height:2px;background:var(--brand-yellow);margin:8px 0 10px}
  .claims__list{list-style:none;display:grid;grid-template-columns:332px auto;row-gap:9px;font-size:18px}
  .claims__list li::before{content:"✓";margin-right:10px}
  .free-from{position:absolute;left:164px;top:966px;width:467px;height:40px;background:var(--brand-yellow);color:var(--sleeve-black);font-weight:700;font-size:16px;display:flex;align-items:center;justify-content:center}
  .weight{position:absolute;left:0;right:0;top:1024px;text-align:center;font-size:21px}
</style>
</head>
<body>
<div class="canvas">
  <section class="sleeve">
    <div class="side-bar side-bar--left"></div>
    <div class="side-bar side-bar--right"></div>

    <div class="seal seal--quality">
      <svg width="26" height="14" viewBox="0 0 26 14"><path d="M1 13 L3 3 L8 8 L13 1 L18 8 L23 3 L25 13 Z" fill="#f7bd1c"/></svg>
      PREMIUM<br>QUALITY
      <div style="font-size:10px;margin-top:3px">★★★</div>
    </div>

    <div class="brand">
      <div class="brand__circle"></div>
      <div class="brand__name">DORVIK</div>
    </div>

    <div class="seal seal--natural">
      <svg width="18" height="14" viewBox="0 0 18 14" style="margin-left:70px"><path d="M2 13 C2 5 8 1 17 1 C16 9 10 13 2 13 Z" fill="#f7bd1c"/></svg>
      NATURAL<br><span class="seal__big">100%</span>
    </div>

    <p class="tagline">PROFESSIONAL HANDMADE WITH PREMIUM INGREDIENTS</p>

    <div class="window-frame"></div>
    <div class="window" role="img" aria-label="Product window showing handmade potato, feta and parsley perogies"></div>

    <div class="flavour-band"></div>
    <h1 class="product-name">PEROGIES</h1>
    <h2 class="flavour">POTATO/FETA/PARSLEY</h2>

    <div class="claims">
      <div class="claims__title">ALL NATURAL</div>
      <div class="claims__rule"></div>
      <ul class="claims__list">
        <li>No Cholesterol</li>
        <li>No Trans Fat</li>
        <li>No Saturated Fat</li>
        <li>Low Sugar</li>
      </ul>
    </div>

    <div class="free-from">No MSG, Preservatives or Artificial ingredients</div>
    <div class="weight">500gm</div>
  </section>
</div>
</body>
</html>
```